we are a mobile auto windscreen replacement business we are looking for a smart, stylish designed card on a matte black base color with large metallic silver KLT (similar to the vexapad box)
over the whole face of the card but down the bottom have (your local automotive & machinery glass specialist) & over the back

Reason: I'm looking for a design like no other something that really wows people to grab a card & use my business

Target Market(s)

Adults in western countries that own an automotive fleet company or anybody that owns a car

Industry/Entity Type

Automotive

Contact Information for Business Card

front: KLTautoglaze
Back: MORRIS 0438 62 57 84 Abn: 52807341196
morris@kltautoglaze.com.au & www.kltautoglaze.com.au

Logo styles of interest
Lettermark Logo
Requirements
Must have
• Metallic font on matte background
Nice to have
• 3D font that's glass or the word KLT smashed into glass on a black background I've added some pictures that maybe you could incorporate in the background or font it would be great to see a professionals ideas

```html
<!DOCTYPE html>
<html lang="en">
<head>
<meta charset="utf-8">
<title>KLT Autoglaze – Business Card</title>
<link rel="stylesheet" href="https://fonts.googleapis.com/css2?family=Montserrat:wght@400;800&family=Crimson+Text:wght@400;600&display=swap">
<style>
  :root {
    --page-bg: #ffffff;
    --card-black: #0b0b0c;
    --card-shadow-tone: #1c1c1f;
    --body-grey: #5a5a5e;
    --sky-grey: #6e6e74;
    --tagline-red: #c8321f;
    --silver-light: #c4c6c9;
    --silver: #8e9094;
    --back-white: #ffffff;
    --back-border: #9a9a9a;
    --ink: #2a2a2a;
    --ink-soft: #555555;
  }
  * { box-sizing: border-box; margin: 0; padding: 0; }
  html, body {
    width: 1200px; height: 1000px; overflow: hidden;
    background: var(--page-bg);
  }
  .sheet { position: relative; width: 1200px; height: 1000px; }
  .card {
    position: absolute; top: 344px;
    width: 540px; height: 312px;
    overflow: hidden;
  }
  /* Front */
  .card--front { left: 40px; background: var(--card-black); }
  .front-visual {
    position: absolute; inset: 0;
    background:
      radial-gradient(ellipse 60% 55% at 50% 55%, var(--body-grey) 0%, var(--card-shadow-tone) 55%, transparent 80%),
      linear-gradient(180deg, var(--sky-grey) 0%, var(--card-shadow-tone) 45%, var(--card-black) 100%);
  }
  .front-logo {
    position: absolute; left: 0; right: 0; top: 126px;
    text-align: center;
    font-family: "Montserrat", sans-serif;
    font-weight: 800;
    font-size: 64px; letter-spacing: 1px; line-height: 1;
    color: var(--silver-light);
  }
  .front-tagline {
    position: absolute; left: 0; right: 0; bottom: 22px;
    text-align: center;
    font-family: "Montserrat", sans-serif;
    font-variant: small-caps;
    font-size: 13px; letter-spacing: 1px;
    color: var(--tagline-red);
  }
  /* Back */
  .card--back {
    left: 620px; background: var(--back-white);
    border: 1px solid var(--back-border);
  }
  .back-logo {
    position: absolute; left: 48px; top: 72px;
    font-family: "Montserrat", sans-serif;
    font-weight: 800;
    font-size: 72px; letter-spacing: 1px; line-height: 1;
    color: var(--silver);
  }
  .back-tagline {
    position: absolute; left: 290px; top: 100px;
    font-family: "Montserrat", sans-serif;
    font-variant: small-caps;
    font-size: 12.5px; letter-spacing: 1.2px; line-height: 1.3;
    color: var(--ink-soft);
  }
  .contact {
    position: absolute; left: 290px; top: 208px;
    font-family: "Crimson Text", serif;
    font-size: 14.5px; line-height: 1.25;
    color: var(--ink-soft);
    list-style: none;
  }
  .contact__name { color: var(--ink); }
  .contact__name strong { font-weight: 600; letter-spacing: 0.5px; margin-right: 12px; }
</style>
</head>
<body>
<main class="sheet">
  <section class="card card--front" aria-label="Business card front">
    <div class="front-visual" role="img" aria-label="Dark studio photograph of a sleek black sports car seen head-on with blue-lit headlights"></div>
    <div class="front-logo">KLT</div>
    <p class="front-tagline">Your Local Automotive &amp; Machinery Glass Specialist</p>
  </section>

  <section class="card card--back" aria-label="Business card back">
    <div class="back-logo">KLT</div>
    <p class="back-tagline">Your Local Automotive &amp;<br>Machinery Glass Specialist</p>
    <ul class="contact">
      <li class="contact__name"><strong>MORRIS</strong>0438 62 57 84</li>
      <li>Abn: 52807341196</li>
      <li>morris@kltautoglaze.com.au</li>
      <li>www.kltautoglaze.com.au</li>
    </ul>
  </section>
</main>
</body>
</html>
```